MOLVT Study flyer

I need help designing a flyer for a research study that will include brain imaging in adolescents. The info is in the attached document. The study is called the Marrowby Orchard Lantern Vesper Trail (MOLVT) study. Ideally this would be returned as a document that I can edit in the future as we will have several new recruitment phases (different age groups, etc. I also would love to have a logo designed as part of this project, but I recognize that might be a separate design request.

```html
<!DOCTYPE html>
<html lang="en">
<head>
<meta charset="utf-8">
<title>MOLVT Study Flyer</title>
<link rel="stylesheet" href="https://fonts.googleapis.com/css2?family=Poppins:wght@400;500;600;700&display=swap">
<style>
  :root {
    --lavender: #e4daf3;
    --paper: #ffffff;
    --purple: #46276a;
    --ink: #1e1a4d;
    --teal: #2bb7a0;
    --teal-deep: #149191;
    --teal-soft: #dcecf1;
    --pink: #d58ba6;
    --uni-blue: #1c4e8f;
    --text: #1a1a1a;
  }
  * { box-sizing: border-box; margin: 0; padding: 0; }
  html, body { width: 930px; height: 1200px; overflow: hidden; }
  body { background: var(--lavender); font-family: "Poppins", sans-serif; color: var(--text); position: relative; }

  .flyer { position: absolute; left: 102px; top: 86px; width: 725px; height: 1027px; background: var(--paper); }
  .abs { position: absolute; }

  /* brand */
  .brand-mark { left: 26px; top: 24px; width: 70px; height: 70px; border-radius: 50%; background: var(--purple); }
  .brand-name { left: 128px; top: 26px; font-size: 47px; font-weight: 700; line-height: 1; color: var(--ink); letter-spacing: 1px; }
  .brand-sub { left: 128px; top: 72px; font-size: 12px; line-height: 14px; color: var(--teal); }

  /* hero */
  .hero { left: 18px; top: 120px; width: 689px; height: 266px; background: var(--purple); border-radius: 33px; }
  .hero-photo { left: 343px; top: 10px; width: 364px; height: 376px; border-radius: 120px 0 33px 0;
    background: linear-gradient(160deg, #d58ba6 0%, #6b3f5a 35%, #c98ab2 55%, #2f4f86 80%, #1f3566 100%); }
  .hero-title { left: 38px; top: 140px; font-size: 38px; font-weight: 600; line-height: 44px; color: #fff; }
  .hero-title .accent { color: var(--teal); }
  .hero-rule { left: 39px; top: 289px; width: 269px; height: 2px; background: #fff; }
  .hero-question { left: 39px; top: 300px; font-size: 24px; font-weight: 600; line-height: 28px; color: #fff; }
  .hero-question .teal { color: var(--teal); }
  .hero-question .pink { color: var(--pink); }

  /* intro */
  .intro { left: 38px; top: 420px; width: 410px; font-size: 17.5px; line-height: 25.5px; color: var(--text); }
  .intro strong { color: var(--purple); font-weight: 600; }
  .intro-divider { left: 466px; top: 422px; width: 1.5px; height: 99px; background: var(--uni-blue); }
  .partner { left: 488px; top: 452px; display: flex; align-items: center; gap: 10px; }
  .partner-dot { width: 36px; height: 36px; border-radius: 50%; background: var(--uni-blue); flex: none; }
  .partner-name { font-size: 18px; font-weight: 600; line-height: 22px; color: var(--uni-blue); }

  /* participation */
  .involves-head { left: 32px; top: 555px; width: 349px; height: 56px; background: var(--teal-deep); border-radius: 22px 22px 0 0;
    color: #fff; font-size: 17.5px; font-weight: 600; text-align: center; padding-top: 12px; }
  .involves-body { left: 25px; top: 603px; width: 363px; height: 229px; background: var(--teal-soft); border-radius: 22px; }
  .involve-item { left: 15px; display: flex; gap: 21px; width: 340px; }
  .involve-icon { width: 43px; height: 43px; flex: none; }
  .involve-title { font-size: 17px; font-weight: 600; color: var(--teal-deep); line-height: 20px; }
  .involve-desc { font-size: 13px; line-height: 14.5px; color: var(--text); }

  /* eligibility */
  .elig-head { left: 420px; top: 577px; font-size: 17.5px; font-weight: 600; line-height: 23px; color: var(--purple); }
  .elig-rule { left: 420px; top: 627px; width: 150px; height: 3px; background: var(--teal-deep); }
  .elig-list { left: 420px; top: 646px; width: 290px; list-style: none; }
  .elig-list li { display: flex; gap: 10px; font-size: 17.5px; line-height: 20px; margin-bottom: 17px; }
  .elig-list svg { width: 23px; height: 23px; flex: none; margin-top: 0; }

  /* footer */
  .footer { left: 0; top: 866px; width: 725px; height: 161px; background: var(--purple); border-radius: 22px 22px 0 0; }
  .mail-badge { left: 26px; top: 882px; width: 44px; height: 44px; border-radius: 50%; background: var(--lavender); }
  .cta { left: 86px; top: 880px; font-size: 24px; font-weight: 600; line-height: 28px; color: #fff; }
  .cta-sub { left: 88px; top: 940px; font-size: 16px; font-weight: 600; color: var(--teal); }
  .email-pill { left: 86px; top: 970px; width: 294px; height: 31px; border-radius: 16px; background: var(--pink);
    color: #fff; font-size: 21px; line-height: 31px; padding-left: 17px; }
  .footer-divider { left: 458px; top: 881px; width: 1.5px; height: 129px; background: #fff; }
  .gift-badge { left: 537px; top: 826px; width: 94px; height: 94px; border-radius: 50%; background: var(--teal); }
  .comp-label { left: 480px; top: 920px; width: 208px; text-align: center; font-size: 21px; color: #fff; }
  .comp-upto { left: 495px; top: 968px; font-size: 16px; font-weight: 500; color: #fff; }
  .comp-amount { left: 543px; top: 946px; font-size: 60px; font-weight: 700; line-height: 1; color: var(--pink); letter-spacing: -1px; }
</style>
</head>
<body>
<main class="flyer">

  <div class="abs brand-mark"></div>
  <div class="abs brand-name">MOLVT</div>
  <div class="abs brand-sub">Marrowby Orchard Lantern<br>Vesper Trail study</div>

  <div class="abs hero"></div>
  <div class="abs hero-photo" role="img" aria-label="Photo of a teenage girl in a pink t-shirt and jeans hugging her knees, with a pink thought bubble containing a heart"></div>
  <h1 class="abs hero-title">Are you the<br>parent of a<br>child age <span class="accent">10-17?</span></h1>
  <div class="abs hero-rule"></div>
  <p class="abs hero-question">Do they worry or <span class="teal">overthink</span><br><span class="pink">negative emotions?</span></p>

  <p class="abs intro">Halvern State University researchers are seeking <strong>girls age 10-17</strong> for a study about brain activity in emotions and decision-making and how they relate to puberty, anxiety and depression.</p>
  <div class="abs intro-divider"></div>
  <div class="abs partner"><span class="partner-dot"></span><span class="partner-name">Halvern State<br>University</span></div>

  <div class="abs involves-head">Study participation involves:</div>
  <div class="abs involves-body"></div>

  <div class="abs involve-item" style="top:623px;left:40px">
    <svg class="involve-icon" viewBox="0 0 43 43" fill="none" stroke="#149191" stroke-width="1.6">
      <circle cx="21.5" cy="21.5" r="20.5"/>
      <circle cx="21.5" cy="20" r="3"/><path d="M16 30c0-4 11-4 11 0z"/>
      <circle cx="14" cy="22" r="2.4"/><circle cx="29" cy="22" r="2.4"/>
      <path d="M9 30c0-3 5-4 7-2M34 30c0-3-5-4-7-2"/>
      <path d="M21.5 16c-5-4-9 1-7 4M21.5 16c5-4 9 1 7 4"/>
    </svg>
    <div><div class="involve-title">One one-hour interview</div><div class="involve-desc">(online or in-person) where your child will discuss their thoughts</div></div>
  </div>
  <div class="abs involve-item" style="top:676px;left:40px">
    <svg class="involve-icon" viewBox="0 0 43 43" fill="none" stroke="#149191" stroke-width="1.6">
      <circle cx="21.5" cy="21.5" r="20.5"/>
      <rect x="12" y="13" width="19" height="16" rx="1.5"/><circle cx="19" cy="19" r="2.6"/>
      <path d="M14.5 27c0-4 9-4 9 0"/><path d="M27 17v8"/>
    </svg>
    <div><div class="involve-title">Online questionnaires</div><div class="involve-desc">(parent and child)</div></div>
  </div>
  <div class="abs involve-item" style="top:727px;left:40px">
    <svg class="involve-icon" viewBox="0 0 43 43" fill="none" stroke="#149191" stroke-width="1.6">
      <circle cx="21.5" cy="21.5" r="20.5"/><circle cx="21.5" cy="21.5" r="17"/>
      <circle cx="21.5" cy="18" r="8"/><circle cx="21.5" cy="18" r="4.5"/>
      <path d="M14 27h15l2 5H12z"/>
    </svg>
    <div><div class="involve-title">One two-hour visit</div><div class="involve-desc">where your child will complete an MRI scan, answer questions about their puberty stage, and have a small hair sample taken to study puberty hormones</div></div>
  </div>

  <h2 class="abs elig-head">Your child may be<br>eligible if they:</h2>
  <div class="abs elig-rule"></div>
  <ul class="abs elig-list">
    <li><svg viewBox="0 0 23 23" fill="none"><path d="M20 11.5A8.5 8.5 0 1 1 14 3.4" stroke="#46276a" stroke-width="2"/><path d="M7 11.5l3.2 3.2L16 8.5" stroke="#46276a" stroke-width="2" stroke-linecap="round" stroke-linejoin="round"/><circle cx="19" cy="4" r="2.6" fill="#2bb7a0"/></svg><span>Are age 10-17</span></li>
    <li><svg viewBox="0 0 23 23" fill="none"><path d="M20 11.5A8.5 8.5 0 1 1 14 3.4" stroke="#46276a" stroke-width="2"/><path d="M7 11.5l3.2 3.2L16 8.5" stroke="#46276a" stroke-width="2" stroke-linecap="round" stroke-linejoin="round"/><circle cx="19" cy="4" r="2.6" fill="#2bb7a0"/></svg><span>Tend to worry or overthink negative thoughts</span></li>
    <li><svg viewBox="0 0 23 23" fill="none"><path d="M20 11.5A8.5 8.5 0 1 1 14 3.4" stroke="#46276a" stroke-width="2"/><path d="M7 11.5l3.2 3.2L16 8.5" stroke="#46276a" stroke-width="2" stroke-linecap="round" stroke-linejoin="round"/><circle cx="19" cy="4" r="2.6" fill="#2bb7a0"/></svg><span>Have not been diagnosed with psychosis, learning problems, or autism</span></li>
  </ul>

  <div class="abs footer"></div>
  <div class="abs mail-badge">
    <svg viewBox="0 0 44 44" width="44" height="44" fill="none">
      <rect x="11" y="15" width="21" height="15" rx="2" stroke="#46276a" stroke-width="2"/>
      <path d="M11 17l10.5 7 10.5-7" stroke="#46276a" stroke-width="2"/>
      <circle cx="31" cy="14" r="3.5" fill="#d58ba6"/>
    </svg>
  </div>
  <p class="abs cta">Interested in participating?<br>Want more information?</p>
  <p class="abs cta-sub">Please contact us!</p>
  <p class="abs email-pill">molvtstudy@halvern.edu</p>
  <div class="abs footer-divider"></div>

  <div class="abs gift-badge">
    <svg viewBox="0 0 94 94" width="94" height="94" fill="none" stroke="#fff" stroke-width="4">
      <rect x="27" y="35" width="40" height="11"/><rect x="30" y="46" width="34" height="24"/>
      <path d="M47 35v35"/><circle cx="41" cy="29" r="4.5"/><circle cx="53" cy="29" r="4.5"/>
    </svg>
  </div>
  <p class="abs comp-label">Compensation</p>
  <p class="abs comp-upto">up to</p>
  <p class="abs comp-amount">$140</p>

</main>
</body>
</html>
```